redesign corporate website (software courses)

We need a complete redesign of the current website: http://t-o-m.example/ (training: http://t-o-m.example/pt-br/treinamento/web ); more clear, different color, navigation, header, footer, whatever (side note: site will be based on bootstrap and drupal). Most important pages:

http://t-o-m.example/pt-br/treinamento (trainingoverviewpage)
http://t-o-m.example/ (frontpage)
http://t-o-m.example/pt-br/treinamento/web (trianingdetailpage)

The design should be valid for further content pages (like http://t-o-m.example/pt-br/desenvolvimentodesoftware) and pages with forms (http://t-o-m.example/pt-br/contact or http://t-o-m.example/pt-br/training/web/register)

Logo attached in white and black and black with shadow.

Some other examples of training sites (just content examples - not as template for similar layout):

http://www.brivatutor.example/packages/4817/Website-Development-Professional-training.html?advid=12&gclid=XQa93kLpr42DFbvn3BqeWTZBqk
http://www.kodewerk-kurse.example/
http://www.lumacod.example/cursos/quill-framework-ii/
http://www.travert-academy.example/lp/php-development-training.aspx?gclid=ZM3rhuPqx51DGTRR8Bpeyk9B2B

Industry/Entity Type

Software

```html
<!DOCTYPE html>
<html lang="pt-BR">
<head>
<meta charset="utf-8">
<title>TOM Technical Online Mastery</title>
<link href="https://fonts.googleapis.com/css2?family=Open+Sans:wght@400;600;700;800&display=swap" rel="stylesheet">
<style>
:root{
  --orange:#f26a1b;
  --orange-dark:#d9540c;
  --orange-light:#f7913f;
  --nav:#3a3a3a;
  --dark:#2b2b2b;
  --footer:#1f1f1f;
  --text:#555;
  --muted:#888;
  --line:#dcdcdc;
  --panel:#f1f1f1;
  --white:#fff;
}
*{box-sizing:border-box;margin:0;padding:0}
html,body{width:849px;height:1200px;overflow:hidden}
body{font-family:"Open Sans",sans-serif;color:var(--text);background:#e9e9e9;font-size:9px;line-height:1.45}
.page{width:849px;height:1200px;position:relative;background:#e9e9e9}
.wrap{width:760px;margin:0 auto;position:relative}

/* header */
.site-header{height:82px;background:var(--white)}
.site-header .wrap{display:flex;align-items:center;justify-content:space-between;height:82px}
.brand{display:flex;align-items:center;gap:10px}
.brand-dot{width:38px;height:38px;border-radius:50%;background:var(--orange)}
.brand-name{font-size:17px;font-weight:700;color:var(--dark);line-height:1.05;width:170px}
.perks{display:flex;gap:10px}
.perk{width:150px;height:44px;background:#f4f4f4;border:1px solid var(--line);padding:6px 10px}
.perk h4{color:var(--orange);font-size:11px;font-weight:600}
.perk p{font-size:7px;color:var(--muted)}

/* nav */
.main-nav{height:28px;background:var(--nav)}
.main-nav .wrap{display:flex;align-items:center;height:28px}
.home-icon{width:14px;height:14px;margin-right:14px}
.main-nav a{color:#eee;text-decoration:none;font-size:9.5px;margin-right:22px;font-weight:600}
.main-nav a.active{color:var(--orange-light)}
.search{margin-left:auto;width:150px;height:17px;background:#fff;border-radius:2px;display:flex;align-items:center;justify-content:space-between;padding:0 6px;font-size:8px;color:#999}

/* hero */
.hero{height:255px;background:linear-gradient(180deg,var(--orange-light),var(--orange) 60%,var(--orange-dark))}
.hero .wrap{height:255px}
.hero h1{position:absolute;left:10px;top:38px;color:#fff;font-size:30px;line-height:1.1;font-weight:800;width:340px}
.hero .lead{position:absolute;left:10px;top:118px;color:#fff;font-size:9px;width:240px}
.btn-join{position:absolute;left:100px;top:175px;background:var(--dark);color:#fff;font-weight:700;font-size:10px;padding:8px 22px;border-radius:3px}
.hero-art{position:absolute;left:380px;top:18px;width:360px;height:215px;border-radius:4px;background:linear-gradient(135deg,#fbd1ac,#e8e8e8 55%,#c9c9c9)}

/* services */
.services{height:120px;background:var(--panel);padding-top:22px}
.services .wrap{display:flex;gap:22px}
.card{flex:1;height:88px;background:#fff;border:1px solid var(--line);position:relative;text-align:center;padding:20px 8px 0}
.card .icon{position:absolute;left:50%;top:-18px;margin-left:-17px;width:34px;height:34px;border-radius:50%;background:#fff;border:2px solid var(--orange);display:flex;align-items:center;justify-content:center}
.card h3{font-size:11px;color:var(--dark);font-weight:600}
.card p{font-size:7px;color:var(--muted);line-height:1.35;margin-top:2px}
.card .more{display:inline-block;margin-top:4px;background:var(--dark);color:#fff;font-size:7px;padding:2px 8px;border-radius:2px}

/* content */
.content{background:#fff;height:520px;padding-top:14px}
.content .wrap{display:flex;gap:26px}
.main-col{width:500px}
.main-col h2{color:var(--orange);font-size:22px;font-weight:600;border-bottom:1px solid var(--line);padding-bottom:2px;margin-bottom:8px}
.main-col p{font-size:8px;margin-bottom:8px;text-align:justify}
.btn-read{display:block;width:50px;margin-left:auto;background:var(--orange);color:#fff;font-size:7.5px;padding:3px 6px;border-radius:2px;text-align:center}
.gallery-title{font-size:13px;font-weight:600;color:var(--dark);margin:22px 0 8px;border-bottom:1px solid var(--line);padding-bottom:3px}
.gallery{display:flex;gap:14px;align-items:center}
.arrow{font-size:12px;color:#aaa}
.thumb{width:104px;height:110px;background:linear-gradient(#e2e2e2,#cfcfcf);border:3px solid #fff;box-shadow:0 0 0 1px var(--line)}
.side-col{width:234px}
.box{border:1px solid var(--line);margin-bottom:12px}
.speak{padding:8px 10px}
.box-title{display:flex;align-items:center;gap:6px;font-size:11px;color:var(--dark);font-weight:600;margin-bottom:5px}
.box-title .bullet{width:16px;height:16px;border-radius:50%;background:var(--orange)}
.speak p{font-size:7.5px;color:var(--muted)}
.speak .who{text-align:right;color:var(--orange);font-size:7.5px;margin-top:3px}
.news{background:var(--panel);padding:10px}
.news .box-title{font-size:13px}
.news p{font-size:7.5px;margin-bottom:6px}
.news .field{display:flex}
.news .field span{flex:1;background:#fff;border:1px solid var(--line);font-size:7.5px;color:#aaa;padding:3px 5px}
.news .field b{background:var(--orange);color:#fff;font-size:7.5px;padding:3px 7px}
.events h3{background:var(--dark);color:#fff;font-size:11px;padding:5px 10px}
.event{display:flex;gap:8px;padding:7px 10px;border-bottom:1px solid var(--line)}
.date{width:30px;height:30px;background:var(--orange);color:#fff;text-align:center;font-size:7px;line-height:1.1;padding-top:5px;font-weight:700}
.event p{font-size:7.5px;color:var(--text)}
.event small{color:var(--muted);font-size:6.5px}

/* footer */
.site-footer{height:167px;background:var(--footer);color:#bbb}
.site-footer .wrap{display:flex;padding-top:16px}
.site-footer h4{color:#fff;font-size:11px;border-bottom:1px solid #444;padding-bottom:4px;margin-bottom:8px}
.contact{width:470px}
.contact p{font-size:8px;line-height:1.6}
.social{flex:1}
.social ul{list-style:none;display:grid;grid-template-columns:1fr 1fr;gap:6px 10px;width:170px}
.social li{display:flex;align-items:center;gap:6px;font-size:8.5px}
.social li i{width:13px;height:13px;background:var(--orange);display:block}
.bottom-bar{position:absolute;left:0;bottom:0;width:849px;height:28px;background:#111}
.bottom-bar .wrap{display:flex;align-items:center;height:28px;font-size:8px;color:#999}
.bottom-bar a{color:#ccc;text-decoration:none;margin-right:16px}
.bottom-bar .copy{margin-left:auto}
</style>
</head>
<body>
<div class="page">
  <header class="site-header">
    <div class="wrap">
      <div class="brand"><span class="brand-dot"></span><span class="brand-name">TOM Technical Online Mastery</span></div>
      <div class="perks">
        <div class="perk"><h4>Competitive Prices</h4><p>Fair prices for every course level</p></div>
        <div class="perk"><h4>Experienced Trainers</h4><p>Certified experts with years of practice</p></div>
      </div>
    </div>
  </header>

  <nav class="main-nav">
    <div class="wrap">
      <svg class="home-icon" viewBox="0 0 14 14"><path d="M1 7 7 1l6 6M3 6v7h3V9h2v4h3V6" fill="none" stroke="#eee" stroke-width="1.4"/></svg>
      <a class="active" href="#">Home</a>
      <a href="#">Treinamento</a>
      <a href="#">Serviços</a>
      <a href="#">Contato</a>
      <a href="#">Localização</a>
      <div class="search"><span>Buscar</span><svg width="9" height="9" viewBox="0 0 9 9"><circle cx="3.8" cy="3.8" r="2.8" fill="none" stroke="#888" stroke-width="1.2"/><path d="M6 6l2.5 2.5" stroke="#888" stroke-width="1.2"/></svg></div>
    </div>
  </nav>

  <section class="hero">
    <div class="wrap">
      <h1>YOUR TAGLINE PLACE HERE INSTITUTE</h1>
      <p class="lead">Lorem Ipsum is simply dummy text of the printing and typesetting industry.</p>
      <span class="btn-join">JOIN NOW</span>
      <div class="hero-art" role="img" aria-label="Laptop, tablet and phone showing the training platform"></div>
    </div>
  </section>

  <section class="services">
    <div class="wrap">
      <div class="card">
        <span class="icon"><svg width="16" height="16" viewBox="0 0 16 16"><rect x="2" y="3" width="12" height="8" fill="none" stroke="#f26a1b" stroke-width="1.4"/><path d="M5 14h6M8 11v3" stroke="#f26a1b" stroke-width="1.4"/></svg></span>
        <h3>Treinamento</h3><p>Cursos profissionais com instrutores experientes para sua equipe e carreira.</p><span class="more">Read more</span>
      </div>
      <div class="card">
        <span class="icon"><svg width="16" height="16" viewBox="0 0 16 16"><path d="M5 4 1 8l4 4M11 4l4 4-4 4M9 3 7 13" fill="none" stroke="#f26a1b" stroke-width="1.4"/></svg></span>
        <h3>Desenvolvimento</h3><p>Criamos software sob medida com foco em qualidade e manutenção simples.</p><span class="more">Read more</span>
      </div>
      <div class="card">
        <span class="icon"><svg width="16" height="16" viewBox="0 0 16 16"><path d="M3 9V7a5 5 0 0 1 10 0v2" fill="none" stroke="#f26a1b" stroke-width="1.4"/><rect x="2" y="8" width="3" height="5" fill="#f26a1b"/><rect x="11" y="8" width="3" height="5" fill="#f26a1b"/></svg></span>
        <h3>Consultoria</h3><p>Apoio técnico para melhorar processos, arquitetura e entregas da empresa.</p><span class="more">Read more</span>
      </div>
      <div class="card">
        <span class="icon"><svg width="16" height="16" viewBox="0 0 16 16"><circle cx="8" cy="8" r="6" fill="none" stroke="#f26a1b" stroke-width="1.4"/><path d="M2 8h12M8 2c-3 3-3 9 0 12M8 2c3 3 3 9 0 12" fill="none" stroke="#f26a1b" stroke-width="1.1"/></svg></span>
        <h3>Curso WEB</h3><p>Aprenda a construir sites modernos com as ferramentas mais usadas hoje.</p><span class="more">Read more</span>
      </div>
    </div>
  </section>

  <section class="content">
    <div class="wrap">
      <div class="main-col">
        <h2>Welcome</h2>
        <p>Lorem Ipsum is simply dummy text of the printing and typesetting industry. Lorem Ipsum has been the industry's standard dummy text ever since the 1500s, when an unknown printer took a galley of type and scrambled it to make a type specimen book. It has survived not only five centuries, but also the leap into electronic typesetting, remaining essentially unchanged. It was popularised in the 1960s with the release of Letraset sheets containing Lorem Ipsum passages, and more recently with desktop publishing software like Aldus PageMaker including versions of Lorem Ipsum.</p>
        <p>Lorem Ipsum is simply dummy text of the printing and typesetting industry. Lorem Ipsum has been the industry's standard dummy text ever since the 1500s, when an unknown printer took a galley of type and scrambled it to make a type specimen book. It has survived not only five centuries, but also the leap into electronic typesetting, remaining essentially unchanged. It was popularised in the 1960s with the release of Letraset sheets containing Lorem Ipsum passages, and more recently with desktop publishing software like Aldus PageMaker including versions of Lorem Ipsum.</p>
        <span class="btn-read">Read more</span>
        <h3 class="gallery-title">Video Gallery</h3>
        <div class="gallery">
          <span class="arrow">&#8249;</span>
          <div class="thumb" role="img" aria-label="Course video preview"></div>
          <div class="thumb" role="img" aria-label="Course video preview"></div>
          <div class="thumb" role="img" aria-label="Course video preview"></div>
          <div class="thumb" role="img" aria-label="Course video preview"></div>
          <span class="arrow">&#8250;</span>
        </div>
      </div>
      <aside class="side-col">
        <div class="box speak">
          <div class="box-title"><span class="bullet"></span>Students Speak Out</div>
          <p>“The course was clear, practical and well paced. The trainers answered every question and the examples matched real projects I work on every day.”</p>
          <p class="who">Ana Ribeiro, developer</p>
        </div>
        <div class="box news">
          <div class="box-title"><span class="bullet"></span>NEWSLETTER</div>
          <p>Enter Your E-mail address and subscribe</p>
          <div class="field"><span>Email address...</span><b>Go</b></div>
        </div>
        <div class="box events">
          <h3>EVENTS/CALENDAR</h3>
          <div class="event"><span class="date">12<br>MAR</span><div><p>Web development bootcamp starts</p><small>Sala 2 — 09:00</small></div></div>
          <div class="event"><span class="date">25<br>MAR</span><div><p>Open day for new students</p><small>Auditório — 14:00</small></div></div>
          <div class="event"><span class="date">08<br>ABR</span><div><p>Advanced PHP workshop</p><small>Sala 1 — 19:00</small></div></div>
        </div>
      </aside>
    </div>
  </section>

  <footer class="site-footer">
    <div class="wrap">
      <div class="contact">
        <h4>GET IN TOUCH</h4>
        <p>Rua das Acácias, 210<br>Jardim Aurora — Vila Serena/SP<br>CEP 19000-000<br>Fone: (18) 3000-0000<br>Celular: (18) 90000-0000<br>contato@t-o-m.example</p>
      </div>
      <div class="social">
        <h4>FOLLOW US</h4>
        <ul>
          <li><i></i>Chatter</li><li><i></i>Linkpro</li>
          <li><i></i>Tweeter</li><li><i></i>Viewtube</li>
        </ul>
      </div>
    </div>
    <div class="bottom-bar">
      <div class="wrap">
        <a href="#">Home</a><a href="#">Treinamento</a><a href="#">Serviços</a><a href="#">Contato</a><a href="#">Localização</a>
        <span class="copy">© 2014 t-o-m.example. All Rights Reserved</span>
      </div>
    </div>
  </footer>
</div>
</body>
</html>
```